Cedar Hall businesscard

We changed our name and logo, now we need new business cards.
3-4/72 Marlow Street Fernvale 2999
www.cedarhall-example.org.au
info@cedarhall-example.org.au
Lorna-Jean Whitcombe
Senior Pastor
ph: 02 95874210

```html
<!DOCTYPE html>
<html lang="en">
<head>
<meta charset="utf-8">
<title>Cedar Hall – Business Card</title>
<link rel="stylesheet" href="https://fonts.googleapis.com/css2?family=Roboto:wght@300;400&display=swap">
<style>
  :root {
    --page-bg: #ffffff;
    --card-bg: #ffffff;
    --slate: #76848f;
    --slate-dark: #3f4f5c;
    --ink-light: #ffffff;
  }
  html, body {
    margin: 0;
    padding: 0;
    width: 1200px;
    height: 827px;
    overflow: hidden;
    background: var(--page-bg);
  }
  .canvas {
    position: relative;
    width: 1200px;
    height: 827px;
  }
  .business-card {
    position: absolute;
    left: 121px;
    top: 108px;
    width: 975px;
    height: 610px;
    background: var(--card-bg);
    box-shadow: 0 0 0 1px #eceeef;
  }
  .business-card svg {
    display: block;
    width: 100%;
    height: 100%;
  }
  .shape-slate { fill: var(--slate); }
  .shape-dark { fill: var(--slate-dark); }
  .card-text {
    font-family: "Roboto", Arial, sans-serif;
    fill: var(--ink-light);
    font-weight: 300;
  }
  .person-name { font-size: 24px; font-weight: 400; }
  .person-role { font-size: 24px; }
  .contact-line { font-size: 22px; }
  .website { font-size: 20.5px; }
  .brand-name { font-size: 15px; letter-spacing: 2px; }
</style>
</head>
<body>
<main class="canvas">
  <article class="business-card">
    <svg viewBox="0 0 731 458" xmlns="http://www.w3.org/2000/svg" aria-labelledby="card-title">
      <title id="card-title">Cedar Hall business card for Lorna-Jean Whitcombe, Senior Pastor</title>
      <defs>
        <clipPath id="card-edge">
          <rect x="0" y="0" width="731" height="458"/>
        </clipPath>
      </defs>

      <g class="background-shapes" clip-path="url(#card-edge)">
        <circle class="shape-slate" cx="481" cy="220" r="290"/>
        <circle class="shape-slate" cx="-25" cy="333" r="124"/>
        <circle class="shape-dark" cx="149" cy="455" r="206"/>
      </g>

      <g class="brand-mark">
        <circle class="shape-slate" cx="109" cy="111" r="78"/>
        <text class="card-text brand-name" x="109" y="116" text-anchor="middle">CEDAR HALL</text>
      </g>

      <g class="person">
        <text class="card-text person-name" x="327" y="106">Lorna-Jean Whitcombe</text>
        <text class="card-text person-role" x="327" y="137">Senior Pastor</text>
      </g>

      <g class="contact">
        <text class="card-text contact-line" x="327" y="294">T : 02 95874210</text>
        <text class="card-text contact-line" x="327" y="322">E : info@cedarhall-example.org.au</text>
        <text class="card-text contact-line" x="327" y="371">3-4/72 Marlow Street Fernvale 2999</text>
      </g>

      <text class="card-text website" x="30" y="370">www.cedarhall-example.org.au</text>
    </svg>
  </article>
</main>
</body>
</html>
```